New Business Card Design For Re-Branded Company (New Logo)

We recently switched our DBA and had a new logo designed. We now need new business cards made around our new logo. We would like to stick with the color scheme in our logo: White, Orange, and Blue. We want to see original bold designs that reflect our position in the solar energy sector but we prefer simple over complicated.

We are curious about vertical designs so if you can translate your design onto a vertical layout we would be open to look at it. We especially like a few designs we have seen on here that are vertical with a black or very dark gray background. They have our logo on one side and then the normal vertical business card on the other side.

I have included a screenshot of one of the samples we like, labeled sample.jpg and a file we were given as an example of our logo on a dark background.

At the same time we are satisfied to stay with what we have always had in a horizontal format. If it's not a lot of extra work for you, designs that are submitted in both horizontal and vertical formats will be greatly appreciated.

Please submit your original, bold, clean designs for consideration. Contact us with any questions or comments that may arise.

Thank you and Good Luck,

RT

```html
<!DOCTYPE html>
<html lang="en">
<head>
<meta charset="utf-8">
<title>Radiant Tide – Business Card</title>
<link href="https://fonts.googleapis.com/css2?family=Open+Sans:wght@400;600;700&display=swap" rel="stylesheet">
<style>
  :root {
    --bg: #2e2e2e;
    --card: #fbfbfa;
    --orange: #ec7d22;
    --blue: #2f7fc4;
    --ink: #1d1d1d;
    --rule: #6d6d6d;
  }
  * { box-sizing: border-box; margin: 0; padding: 0; }
  html, body { width: 1200px; height: 929px; overflow: hidden; }
  body {
    background: var(--bg);
    font-family: "Open Sans", Arial, sans-serif;
    position: relative;
  }
  .card {
    position: absolute;
    width: 640px;
    height: 366px;
    background: var(--card);
    border-radius: 3px;
    box-shadow: 0 6px 18px rgba(0,0,0,.35);
    overflow: hidden;
  }
  .card--back { left: 280px; top: 52px; }
  .card--front { left: 280px; top: 480px; }

  .brand {
    display: flex;
    align-items: center;
    gap: 12px;
    font-weight: 700;
    color: var(--blue);
    letter-spacing: .5px;
    text-transform: uppercase;
  }
  .brand__dot {
    border-radius: 50%;
    border: 5px solid var(--orange);
    flex: none;
  }
  .card--back .brand {
    position: absolute;
    left: 0; right: 0; top: 150px;
    justify-content: center;
    font-size: 44px;
  }
  .card--back .brand__dot { width: 52px; height: 52px; }

  .card--front .brand {
    position: absolute;
    left: 28px; top: 140px;
    font-size: 25px;
    gap: 9px;
  }
  .card--front .brand__dot { width: 32px; height: 32px; border-width: 4px; }

  .divider {
    position: absolute;
    left: 262px; top: 36px;
    width: 1px; height: 220px;
    background: var(--rule);
  }
  .person { position: absolute; left: 290px; top: 38px; }
  .person__name { color: var(--blue); font-size: 28px; font-weight: 400; line-height: 1.1; }
  .person__title { color: var(--ink); font-size: 17px; margin-top: 2px; }

  .contacts {
    position: absolute;
    left: 292px; top: 138px;
    list-style: none;
  }
  .contacts li {
    display: flex; align-items: center; gap: 10px;
    font-size: 15px; color: var(--ink);
    height: 22px;
  }
  .contacts svg { width: 13px; height: 13px; flex: none; }

  .band { position: absolute; left: 0; top: 0; width: 640px; height: 366px; }
</style>
</head>
<body>
  <section class="card card--back" aria-label="Card back">
    <div class="brand"><span class="brand__dot"></span>Radiant Tide</div>
  </section>

  <section class="card card--front" aria-label="Card front">
    <svg class="band" viewBox="0 0 640 366" aria-hidden="true">
      <path d="M150 340 C 320 270, 480 245, 640 232 L640 250 C 480 262, 330 285, 150 340 Z" fill="var(--orange)"/>
      <path d="M110 366 C 300 290, 470 262, 640 250 L640 366 Z" fill="var(--blue)"/>
      <text x="470" y="338" text-anchor="middle" fill="#fff" font-family="Open Sans, Arial, sans-serif" font-size="17" transform="rotate(-9 470 338)">480 Linden Row, Fairview, TN 37010</text>
    </svg>

    <div class="brand"><span class="brand__dot"></span>Radiant Tide</div>
    <div class="divider"></div>

    <div class="person">
      <p class="person__name">Martin Ellsworth</p>
      <p class="person__title">Founder/CEO</p>
    </div>

    <ul class="contacts">
      <li><svg viewBox="0 0 13 13"><rect width="13" height="13" rx="2" fill="var(--orange)"/><path d="M3.5 3h2l.6 2-1 .8a5 5 0 0 0 2 2l.8-1 2 .6v2c-4 .3-6.7-2.4-6.4-6.4z" fill="#fff"/></svg>555-210-4417</li>
      <li><svg viewBox="0 0 13 13"><rect width="13" height="13" rx="2" fill="var(--orange)"/><rect x="4" y="2.5" width="5" height="8" rx="1" fill="#fff"/></svg>555-318-6620</li>
      <li><svg viewBox="0 0 13 13"><rect width="13" height="13" rx="2" fill="var(--orange)"/><rect x="3" y="5" width="7" height="4.5" fill="#fff"/><rect x="4.5" y="3" width="4" height="2" fill="#fff"/></svg>555-210-4419</li>
      <li><svg viewBox="0 0 13 13"><rect width="13" height="13" rx="2" fill="var(--orange)"/><circle cx="6.5" cy="6.5" r="3.5" fill="none" stroke="#fff" stroke-width="1.3"/></svg>hello@radianttide.com</li>
      <li><svg viewBox="0 0 13 13"><rect width="13" height="13" rx="2" fill="var(--orange)"/><rect x="3" y="4" width="7" height="5" fill="#fff"/><path d="M3 4l3.5 3L10 4" fill="none" stroke="var(--orange)" stroke-width="1"/></svg>www.radianttide.com</li>
    </ul>
  </section>
</body>
</html>
```